Managed Service Provider VOIP Flyer

Looking for a one page US letter size single or double sided brochure to offer cloud hosted VoIP Phone system and unified communications. We have partnered with a VoIP Phone system company and want to sell their services but we don't want their name to be shown on the brochure because customers might call them directly. The company name is Quorvel (www.quorvel-example.com) and our company name is Lumen By Harlow, LLC and our voice product is called Clearly Talk. I have also uploaded my company's logo that you should show on the brochure and use that coloring. For more details about the product, you can visit their website mentioned above. Also I am looking for something very similar to this project and many of the technical details are the same https://flyer.contestpad-example.com/contest/5817264

I have also uploaded a PDF with my different package levels and some of the included features. Depending on the design we may or may not want the package levels on this flyer.

Target Market(s)

Small and medium Businesses

Industry/Entity Type

Voip

Requirements
Must have
• Feature and benefits information of Managed VOICE. Use my logo and coloring from my logo. Include our website, email, phone and possibly facebook if it makes sense/looks good.

www.lumenbyharlow-example.com
415.836.0.917
sales@lumenbyharlow-example.com
www.socialsite-example.com/lumenbyharlow
Nice to have
• Would like to show how the service is simple and reliable and available for any business size

```html
<!DOCTYPE html>
<html lang="en">
<head>
<meta charset="utf-8">
<title>Clearly Talk – Managed Voice Flyer</title>
<link href="https://fonts.googleapis.com/css2?family=Josefin+Sans:wght@400;600;700&display=swap" rel="stylesheet">
<style>
  :root{
    --navy:#1f3a6b;
    --navy-deep:#1a2f58;
    --red:#d2252b;
    --ink:#111;
    --dark:#0d131f;
    --paper:#fff;
    --backdrop:#8a8a8a;
  }
  *{box-sizing:border-box;margin:0;padding:0}
  html,body{width:1200px;height:806px;overflow:hidden}
  body{background:var(--backdrop);font-family:"Josefin Sans",sans-serif;color:var(--ink);position:relative}

  .page{position:absolute;top:33px;width:572px;height:740px;background:var(--paper);overflow:hidden}
  .page-front{left:18px}
  .page-back{left:610px}

  /* brand */
  .brand{position:absolute;display:flex;align-items:center;gap:7px;color:var(--navy);font-weight:700;letter-spacing:.5px}
  .brand-mark{background:var(--red)}
  .brand-top{left:0;right:0;top:26px;justify-content:center;font-size:17px}
  .brand-top .brand-mark{width:18px;height:18px}
  .brand-footer{left:17px;top:676px;font-size:21px}
  .brand-footer .brand-mark{width:26px;height:26px}

  /* hero band */
  .hero-band{position:absolute;left:0;top:0;width:572px;height:240px}
  .hero-photo{position:absolute;left:250px;top:0;width:322px;height:240px;
    clip-path:polygon(0 74px,31px 79px,322px 36px,322px 184px,31px 226px,0 222px);
    background:radial-gradient(ellipse 120px 90px at 180px 110px,#3b7fb5 0%,#1c4473 45%,rgba(16,28,48,0) 100%),
               linear-gradient(90deg,#0d131f 0%,#17263f 40%,#1b3252 100%)}
  .hero-copy{position:absolute;left:16px;top:83px;color:#fff;font-weight:700;text-transform:uppercase}
  .hero-lead{font-size:15.5px;line-height:18px;letter-spacing:.6px}
  .hero-accent{color:var(--red);font-size:20.5px;line-height:22px;margin-top:2px;letter-spacing:.4px}
  .hero-tail{font-size:10px;letter-spacing:2.4px;margin-top:1px}

  /* seat features */
  .section-title{position:absolute;left:0;right:0;text-align:center;font-weight:700;color:var(--navy)}
  .section-title .hl{color:var(--red)}
  .seat-title{top:256px;font-size:19px;letter-spacing:.5px}

  .feature{position:absolute}
  .col-left{left:0;width:254px}
  .col-right{left:285px;width:270px}
  .feature-tab{display:flex;height:19px}
  .tab-mark{width:32px;height:19px;background:var(--red);display:flex;align-items:center;justify-content:center;
    clip-path:polygon(0 0,100% 0,calc(100% - 5px) 100%,0 100%)}
  .tab-label{height:19px;line-height:21px;background:var(--navy);color:#fff;font-size:11px;letter-spacing:.4px;
    padding:0 16px 0 10px;margin-left:-2px;clip-path:polygon(5px 0,calc(100% - 9px) 0,100% 100%,0 100%)}
  .feature-text{font-size:9.4px;line-height:10.8px;text-align:justify;margin-top:9px}
  .col-left .feature-text{margin-left:36px}
  .col-right .feature-text{margin-left:28px}

  /* back page */
  .back-top{position:absolute;left:0;top:0;width:572px;height:330px;
    background:radial-gradient(ellipse 160px 90px at 470px 300px,#bfc3c8 0%,rgba(230,232,235,0) 100%),
               linear-gradient(180deg,#f7f8f9 0%,#eef0f2 60%,#dfe2e6 100%)}
  .pbx-title{top:30px;font-size:18.5px;letter-spacing:1px}
  .pbx-item{position:absolute;width:248px}
  .pbx-head{display:flex;align-items:center;gap:7px;color:var(--navy);font-weight:700;font-size:12px;letter-spacing:.3px}
  .pbx-text{margin-left:20px;margin-top:4px;font-size:9.3px;line-height:12.3px;text-align:justify;color:#1a1a1a}

  .addon-band{position:absolute;left:0;top:300px;width:572px;height:360px}
  .addon-ribbon{position:absolute;left:165px;top:313px;width:232px;height:37px;display:flex;align-items:center;justify-content:center;
    color:#fff;font-weight:700;font-size:16.5px;letter-spacing:.8px}
  .addon-ribbon svg{position:absolute;inset:0}
  .addon-ribbon span{position:relative;padding-top:3px}
  .addon{position:absolute;top:392px;color:#fff;width:122px}
  .addon-icon{height:42px;display:flex;align-items:flex-end}
  .addon-title{font-size:13px;line-height:14px;margin-top:12px;letter-spacing:.3px}
  .addon-text{font-size:9.3px;line-height:12.3px;margin-top:9px}

  .contact{position:absolute;left:330px;top:662px}
  .contact-title{color:var(--red);font-size:16px;letter-spacing:.8px}
  .contact-line{display:flex;align-items:center;gap:9px;color:var(--navy);font-size:11px;font-weight:600;margin-top:5px}
</style>
</head>
<body>
<svg width="0" height="0" style="position:absolute">
  <defs>
    <symbol id="tick-white" viewBox="0 0 14 14">
      <path d="M12 6.5A5.2 5.2 0 1 1 9.6 2.3" fill="none" stroke="#fff" stroke-width="1.6" stroke-linecap="round"/>
      <path d="M4.3 6.6l2.4 2.4 6-6.2" fill="none" stroke="#fff" stroke-width="1.7" stroke-linecap="round" stroke-linejoin="round"/>
    </symbol>
    <symbol id="tick-red" viewBox="0 0 14 14">
      <path d="M12 6.5A5.2 5.2 0 1 1 9.6 2.3" fill="none" stroke="#d2252b" stroke-width="1.6" stroke-linecap="round"/>
      <path d="M4.3 6.6l2.4 2.4 6-6.2" fill="none" stroke="#d2252b" stroke-width="1.7" stroke-linecap="round" stroke-linejoin="round"/>
    </symbol>
  </defs>
</svg>

<!-- FRONT -->
<section class="page page-front">
  <svg class="hero-band" viewBox="0 0 572 240">
    <polygon points="0,36 281,79 572,36 572,184 281,226 0,184" fill="#0d131f"/>
    <polygon points="0,184 281,226 572,184 572,194 281,238 0,194" fill="#d2252b"/>
  </svg>
  <div class="hero-photo" role="img" aria-label="Open hands holding a glowing cloud circuit chip"></div>

  <div class="brand brand-top"><span class="brand-mark"></span>LUMEN BY HARLOW</div>

  <div class="hero-copy">
    <p class="hero-lead">Would like to<br>show how the service</p>
    <p class="hero-accent">Simple and reliable<br>and available</p>
    <p class="hero-tail">For anybusiness size</p>
  </div>

  <h2 class="section-title seat-title"><span class="hl">SEAT</span> FEATURES</h2>

  <div class="feature col-left" style="top:296px">
    <div class="feature-tab"><span class="tab-mark"><svg width="12" height="12"><use href="#tick-white"/></svg></span><span class="tab-label">3-Way Calling</span></div>
    <p class="feature-text">With a 3-Way Call, or an ad-hoc conference, you can bring two other lines (internal and/or external) into a call with you.</p>
  </div>
  <div class="feature col-left" style="top:363px">
    <div class="feature-tab"><span class="tab-mark"><svg width="12" height="12"><use href="#tick-white"/></svg></span><span class="tab-label">Call Logs</span></div>
    <p class="feature-text">Your administrator will have access to view call detail records, such as inbound and outbound calls, time, and duration.</p>
  </div>
  <div class="feature col-left" style="top:431px">
    <div class="feature-tab"><span class="tab-mark"><svg width="12" height="12"><use href="#tick-white"/></svg></span><span class="tab-label">Call Waiting</span></div>
    <p class="feature-text">Call waiting allows you to receive a new call while you are still on an existing call.</p>
  </div>
  <div class="feature col-left" style="top:485px">
    <div class="feature-tab"><span class="tab-mark"><svg width="12" height="12"><use href="#tick-white"/></svg></span><span class="tab-label">Call Forward Always</span></div>
    <p class="feature-text">Forward all incoming calls to another extension or phone number.</p>
  </div>
  <div class="feature col-left" style="top:542px">
    <div class="feature-tab"><span class="tab-mark"><svg width="12" height="12"><use href="#tick-white"/></svg></span><span class="tab-label">Call Forward No Answer</span></div>
    <p class="feature-text">Forward unanswered calls to an extension or phone number other than the voicemail after a set number of rings (default 3).</p>
  </div>
  <div class="feature col-left" style="top:610px">
    <div class="feature-tab"><span class="tab-mark"><svg width="12" height="12"><use href="#tick-white"/></svg></span><span class="tab-label">Call Forward Not Reachable</span></div>
    <p class="feature-text">In the event that you lose your internet service, you can set a number to forward calls to when your phone is offline.</p>
  </div>
  <div class="feature col-left" style="top:677px">
    <div class="feature-tab"><span class="tab-mark"><svg width="12" height="12"><use href="#tick-white"/></svg></span><span class="tab-label">Caller ID and Caller Name Delivery</span></div>
    <p class="feature-text">Incoming calls will include the incoming caller ID and caller name if provided by the network.</p>
  </div>

  <div class="feature col-right" style="top:296px">
    <div class="feature-tab"><span class="tab-mark"><svg width="12" height="12"><use href="#tick-white"/></svg></span><span class="tab-label">Do Not Disturb</span></div>
    <p class="feature-text">Placing your phone service in Do Not Disturb will cause all calls to go to your voicemail box or specified busy treatment.</p>
  </div>
  <div class="feature col-right" style="top:369px">
    <div class="feature-tab"><span class="tab-mark"><svg width="12" height="12"><use href="#tick-white"/></svg></span><span class="tab-label">Extension Dialing</span></div>
    <p class="feature-text">You may call other phones in your PBX with an extension, even if they are in other locations.</p>
  </div>
  <div class="feature col-right" style="top:431px">
    <div class="feature-tab"><span class="tab-mark"><svg width="12" height="12"><use href="#tick-white"/></svg></span><span class="tab-label">Last Number Redial</span></div>
    <p class="feature-text">You can redial the last number you called.</p>
  </div>
  <div class="feature col-right" style="top:481px">
    <div class="feature-tab"><span class="tab-mark"><svg width="12" height="12"><use href="#tick-white"/></svg></span><span class="tab-label">Simultaneous Ring</span></div>
    <p class="feature-text">You can specify extensions and numbers to ring at the same time as the desk line extension.</p>
  </div>
  <div class="feature col-right" style="top:540px">
    <div class="feature-tab"><span class="tab-mark"><svg width="12" height="12"><use href="#tick-white"/></svg></span><span class="tab-label">Sequential Ring</span></div>
    <p class="feature-text">A sequence of extensions and numbers can be set up to dial if the desk phone does not pick up.</p>
  </div>
  <div class="feature col-right" style="top:603px">
    <div class="feature-tab"><span class="tab-mark"><svg width="12" height="12"><use href="#tick-white"/></svg></span><span class="tab-label">Speed Dial 100</span></div>
    <p class="feature-text">You can specify up to 100 number to dial with #xx with the dial pad.</p>
  </div>
  <div class="feature col-right" style="top:665px">
    <div class="feature-tab"><span class="tab-mark"><svg width="12" height="12"><use href="#tick-white"/></svg></span><span class="tab-label">Unified Messaging</span></div>
    <p class="feature-text">Your seat has voicemail included, but can also be configured for voicemail to email, zero-out, and email notifications.</p>
  </div>
</section>

<!-- BACK -->
<section class="page page-back">
  <div class="back-top" role="img" aria-label="Faded office desk with a desk phone"></div>

  <h2 class="section-title pbx-title">ALL <span class="hl">PBX</span> INCLUDE THE FOLLOWING FEATURES</h2>

  <div class="pbx-item" style="left:15px;top:70px">
    <h3 class="pbx-head"><svg width="13" height="13"><use href="#tick-red"/></svg>Auto Attendant</h3>
    <p class="pbx-text">An automated recording that answers the phone and provides a personalized message to callers with options for connecting to the operator, dialing by name or extension, or connecting to up to nine configurable extensions. Configuration via the Customer Portal allows for hours of operation to be modified, with different options available for hours that the company is open or closed.</p>
  </div>
  <div class="pbx-item" style="left:15px;top:208px">
    <h3 class="pbx-head"><svg width="13" height="13"><use href="#tick-red"/></svg>Company Main Number</h3>
    <p class="pbx-text" style="margin-top:7px">Phone number with unlimited incoming minutes that can be configured to point to any group extension in the PBX (such as an auto attendant or hunt group).</p>
  </div>
  <div class="pbx-item" style="left:290px;top:70px">
    <h3 class="pbx-head"><svg width="13" height="13"><use href="#tick-red"/></svg>Corporate Directory</h3>
    <p class="pbx-text">System Users are networked for extension to extension calling</p>
  </div>
  <div class="pbx-item" style="left:290px;top:122px">
    <h3 class="pbx-head"><svg width="13" height="13"><use href="#tick-red"/></svg>Hunt Groups</h3>
    <p class="pbx-text">Allows users within a group to be included in a specified subgroup to handle incoming calls received by an assigned Hunt Group’s phone number. Within the Customer Portal, company administrators can choose from “hunt” schemes, each of which rings the specified phones in a different manner.</p>
  </div>
  <div class="pbx-item" style="left:290px;top:225px">
    <h3 class="pbx-head"><svg width="13" height="13"><use href="#tick-red"/></svg>Music on Hold</h3>
    <p class="pbx-text">Enables company administrators to upload an audio file (.wav file containing music, advertising, etc.) onto the system to be broadcast to parties while on hold.</p>
  </div>

  <svg class="addon-band" viewBox="0 300 572 360" role="img" aria-label="City towers in a deep blue tint">
    <defs>
      <linearGradient id="addonFill" x1="0" y1="0" x2="0" y2="1">
        <stop offset="0" stop-color="#223f73"/>
        <stop offset="1" stop-color="#1b335f"/>
      </linearGradient>
    </defs>
    <polygon points="0,305 572,305 572,590 281,632 0,590" fill="url(#addonFill)"/>
    <polygon points="0,590 281,632 572,590 572,599 281,647 0,599" fill="#d2252b"/>
  </svg>

  <div class="addon-ribbon">
    <svg viewBox="0 0 232 37" preserveAspectRatio="none">
      <polygon points="14,0 218,0 232,18.5 218,37 14,37 0,18.5" fill="#d2252b"/>
      <polygon points="16,3 216,3 228,18.5 216,34 16,34 4,18.5" fill="none" stroke="#fff" stroke-width="1"/>
    </svg>
    <span>ADD-ON FEATURES</span>
  </div>

  <div class="addon" style="left:17px">
    <div class="addon-icon">
      <svg width="40" height="34" viewBox="0 0 40 34" fill="none" stroke="#d2252b" stroke-width="2">
        <rect x="2" y="2" width="8" height="30" rx="3"/>
        <rect x="10" y="4" width="28" height="28" rx="3"/>
        <rect x="15" y="8" width="18" height="6"/>
        <path d="M15 19h3M21 19h3M27 19h3M15 23h3M21 23h3M27 23h3M15 27h3M21 27h3M27 27h3"/>
      </svg>
    </div>
    <h3 class="addon-title">Advanced Auto<br>Attendant</h3>
    <p class="addon-text">A multi-level Auto Attendant (for example, enterprise’s main Auto Attendant is configured to seamlessly route to the Auto Attendant of a particular department or location).</p>
  </div>
  <div class="addon" style="left:163px">
    <div class="addon-icon">
      <svg width="40" height="34" viewBox="0 0 40 34" fill="none" stroke="#d2252b" stroke-width="2">
        <path d="M5 4c-3 2-3 7 1 13s10 12 15 14c3 1 5 0 7-2l-5-5-4 2c-3-2-6-6-8-9l2-4-5-5z" stroke-linejoin="round"/>
        <text x="20" y="9" font-size="8.5" font-family="Josefin Sans, sans-serif" font-weight="700" fill="#d2252b" stroke="none">REC</text>
      </svg>
    </div>
    <h3 class="addon-title">Call Recording</h3>
    <p class="addon-text">Allows a user to record their calls in either an always on or ondemand mode. These recording capabilities can allow for personal monitoring or supervised monitoring of recorded calls</p>
  </div>
  <div class="addon" style="left:307px">
    <div class="addon-icon">
      <svg width="30" height="36" viewBox="0 0 30 36" fill="#d2252b">
        <circle cx="5" cy="4" r="2.6"/><circle cx="15" cy="4" r="2.6"/><circle cx="25" cy="4" r="2.6"/>
        <circle cx="5" cy="13" r="2.6"/><circle cx="15" cy="13" r="2.6"/><circle cx="25" cy="13" r="2.6"/>
        <circle cx="5" cy="22" r="2.6"/><circle cx="15" cy="22" r="2.6"/><circle cx="25" cy="22" r="2.6"/>
        <circle cx="15" cy="31" r="2.6"/>
      </svg>
    </div>
    <h3 class="addon-title">Toll-Free Numbers</h3>
    <p class="addon-text">An “800” number with inbound calling charged a toll to you, not the caller</p>
  </div>
  <div class="addon" style="left:449px">
    <div class="addon-icon">
      <svg width="30" height="40" viewBox="0 0 30 40" fill="none" stroke="#d2252b" stroke-width="1.6">
        <circle cx="9" cy="3" r="2"/><circle cx="17" cy="3" r="2"/><circle cx="25" cy="3" r="2"/>
        <circle cx="9" cy="10" r="2"/><circle cx="17" cy="10" r="2"/><circle cx="25" cy="10" r="2"/>
        <circle cx="17" cy="17" r="2"/><circle cx="25" cy="17" r="2"/>
        <path d="M7 13v14l-3-3-2 2 5 8h12l2-8v-6l-4-1v-2l-4-1v-1l-4-1v-2" stroke-linejoin="round"/>
      </svg>
    </div>
    <h3 class="addon-title">Virtual Number</h3>
    <p class="addon-text">Additional phone number with unlimited incoming minutes that can be configured to point to any extension in the PBX.</p>
  </div>

  <div class="brand brand-footer"><span class="brand-mark"></span>LUMEN BY HARLOW</div>

  <div class="contact">
    <h3 class="contact-title">CONTACT US</h3>
    <p class="contact-line">
      <svg width="10" height="10" viewBox="0 0 10 10"><path d="M1.5 1c-1 .7-1 2.3.3 4.2s3 3.5 4.5 4c1 .3 1.6 0 2.2-.6L7 7.1l-1.3.6C4.8 7.1 3.9 6 3.3 5l.6-1.3L2.4 2z" fill="#d2252b"/></svg>
      415.836.0.917</p>
    <p class="contact-line">
      <svg width="10" height="8" viewBox="0 0 10 8"><rect width="10" height="8" fill="#d2252b"/><path d="M0 0l5 4 5-4" fill="none" stroke="#fff" stroke-width="1"/></svg>
      sales@lumenbyharlow-example.com</p>
    <p class="contact-line">
      <svg width="10" height="10" viewBox="0 0 10 10" fill="none" stroke="#d2252b" stroke-width="1"><circle cx="5" cy="5" r="4.3"/><ellipse cx="5" cy="5" rx="1.9" ry="4.3"/><path d="M.7 5h8.6M1.5 2.8h7M1.5 7.2h7"/></svg>
      www.lumenbyharlow-example.com</p>
  </div>
</section>
</body>
</html>
```